Professional Price List Design for Luxury Candle Range (Print-Ready)

This project requires a luxury, calm, high-end price list — not a flyer, not a basic price sheet. I am wanting mainly soft whites, warm creams, beige, subtle gold tones - no bold colours. Layout to be clearly sectioned by candle range; each range must read as a distinct feature, while flowing cohesively on one page (ideally without looking cramped).
Use clean margins and balanced spacing.
Overall layout should resemble a boutique catalogue or luxury menu
Use some of the supplied candle images only, true to size (no distortion)
Elegant, refined typography is essential

If this style or level of refinement is not aligned with your design approach, please do not submit an entry.

Target Market(s)

Individuals interested in wellness, mindfulness, and soulful living

Industry/Entity Type

Wellness & Lifestyle Brand

Colors

Designer to choose colors to be used in the design.

Requirements
Must have
• A design that allows for future updates as new products are released. Contact email clearly visible for ordering
Nice to have
• Some snap shots of each different candle ranges - I have attached individual photos to brief - they DO NOT all have to be included, they are just examples in case you want to use them.
Should not have
• No loud colours. No crowded pricing or tight spacing.

```html
<!DOCTYPE html>
<html lang="en">
<head>
<meta charset="utf-8">
<title>Candle Collection Pricelist</title>
<link rel="stylesheet" href="https://fonts.googleapis.com/css2?family=Gilda+Display&family=Montserrat:wght@300;400;700&display=swap">
<style>
  :root{
    --backdrop:#f8f6f1;
    --card:#f8f6f2;
    --olive:#5c6b2a;
    --olive-line:#7b8748;
    --text:#4a4a44;
    --sage-light:#e3f1e3;
    --sage:#bfe0c4;
    --white:#ffffff;
    --brand:#4a2e1c;
  }
  *{margin:0;padding:0;box-sizing:border-box;}
  html,body{width:1200px;height:960px;overflow:hidden;background:var(--backdrop);}
  .canvas{position:relative;width:1200px;height:960px;}
  .page{position:absolute;top:119px;width:510px;height:721px;
    box-shadow:6px 8px 14px rgba(0,0,0,.18);}
  .page--left{left:79px;}
  .page--right{left:629px;}
  .wash{position:absolute;inset:0;
    background:
      radial-gradient(ellipse 60% 45% at 15% 20%, var(--sage) 0%, transparent 70%),
      radial-gradient(ellipse 45% 40% at 90% 70%, var(--sage-light) 0%, transparent 75%),
      radial-gradient(ellipse 70% 30% at 40% 98%, var(--sage) 0%, transparent 70%),
      linear-gradient(160deg, var(--sage-light) 0%, var(--white) 55%, var(--sage-light) 100%);}
  .card{position:absolute;left:30px;top:30px;width:449px;height:660px;
    background:var(--card);border-radius:22px;
    box-shadow:3px 5px 10px rgba(0,0,0,.12);}
  .card > *{position:absolute;left:0;width:100%;text-align:center;}
  .eyebrow{font-family:"Gilda Display",serif;font-weight:400;font-size:12px;letter-spacing:2px;color:var(--olive);}
  .title{font-family:"Gilda Display",serif;font-weight:400;font-size:36px;line-height:1;letter-spacing:5px;padding-left:5px;color:var(--olive);}
  .title-rule{height:10px;}
  .range-name{font-family:"Gilda Display",serif;font-weight:400;font-size:11px;letter-spacing:1.8px;color:var(--olive);}
  .range-copy{font-family:"Montserrat",sans-serif;font-weight:300;font-size:9.4px;line-height:10.3px;color:var(--text);}
  .prices{font-family:"Montserrat",sans-serif;font-weight:700;font-size:8.4px;line-height:12px;color:var(--olive);}
  .divider{left:26px;width:396px;height:1px;background:var(--olive-line);opacity:.8;}
  .email{font-weight:700;font-size:10.5px;color:var(--olive);}
  .brand{font-family:"Montserrat",sans-serif;font-weight:300;font-size:20px;letter-spacing:4px;color:var(--brand);line-height:1;}
</style>
</head>
<body>
<div class="canvas">

  <article class="page page--left">
    <div class="wash" role="img" aria-label="Soft green watercolour wash with faint eucalyptus leaves"></div>
    <div class="card">
      <p class="eyebrow" style="top:42px;">CANDLE COLLECTION</p>
      <h1 class="title" style="top:61px;">PRICELIST</h1>
      <svg class="title-rule" style="top:74px;" width="449" height="10" viewBox="0 0 449 10" aria-hidden="true">
        <line x1="40" y1="5" x2="112" y2="5" stroke="#5c6b2a" stroke-width="1"/>
        <path d="M112 1 L116 5 L112 9 L108 5 Z" fill="#5c6b2a"/>
        <path d="M333 1 L337 5 L333 9 L329 5 Z" fill="#5c6b2a"/>
        <line x1="337" y1="5" x2="409" y2="5" stroke="#5c6b2a" stroke-width="1"/>
      </svg>

      <h2 class="range-name" style="top:131px;">CORE LUXURY RANGE</h2>
      <p class="range-copy" style="top:152px;">Poured into beautiful, statement vessels, the Core<br>Luxury Range features timeless jars designed to<br>bring warmth, calm, and quiet luxury into your space.</p>
      <p class="prices" style="top:193px;">Crystal Riviera – Luxury Jar – 400g — $50</p>
      <div class="divider" style="top:217px;"></div>

      <h2 class="range-name" style="top:235px;">SIGNATURE INSPIRATION RANGE</h2>
      <p class="range-copy" style="top:260px;">These candles are more than scent — they are gentle<br>reminders. Of your worth. Of your strength. Of the<br>importance of choosing moments that nourish you.</p>
      <p class="prices" style="top:297px;">Heritage Amber Jar – Bamboo Lid – 295g — $30<br>Opal Dome Jar – 200g — $40</p>
      <div class="divider" style="top:334px;"></div>

      <h2 class="range-name" style="top:355px;">EVERYDAY ESSENTIALS</h2>
      <p class="range-copy" style="top:380px;">Simple, comforting candles designed for daily<br>moments of calm and warmth.</p>
      <p class="prices" style="top:417px;">Amber Jar – 150g — $20</p>
      <div class="divider" style="top:450px;"></div>

      <h2 class="range-name" style="top:461px;">SUGAR ROW RANGE</h2>
      <p class="range-copy" style="top:486px;">A deliciously indulgent collection that looks almost good<br>enough to eat and smells absolutely divine. The Sugar<br>Row Collection fills your space with rich, comforting<br>fragrance — a sweet sensory escape.</p>
      <p class="prices" style="top:536px;">Strawberry Milkshake – 235g — $35<br>Chocolate Milkshake – 235g — $35<br>Caramel Popcorn – 295g — $30<br>Iced Coffee – 295g — $30<br>Café Latte – 295g — $30</p>
    </div>
  </article>

  <article class="page page--right">
    <div class="wash" role="img" aria-label="Soft green watercolour wash with faint eucalyptus leaves"></div>
    <div class="card">
      <p class="eyebrow" style="top:42px;">CANDLE COLLECTION</p>
      <h1 class="title" style="top:61px;">PRICELIST</h1>
      <svg class="title-rule" style="top:74px;" width="449" height="10" viewBox="0 0 449 10" aria-hidden="true">
        <line x1="40" y1="5" x2="116" y2="5" stroke="#5c6b2a" stroke-width="1"/>
        <line x1="333" y1="5" x2="409" y2="5" stroke="#5c6b2a" stroke-width="1"/>
      </svg>

      <h2 class="range-name" style="top:131px;">BABY &amp; KEEPSAKE RANGE</h2>
      <p class="range-copy" style="top:152px;">Created to celebrate new life, this range is a soft<br>welcome into the world. Gentle, meaningful candles<br>designed to honour love, beginnings, and the light<br>each little soul brings.</p>
      <p class="prices" style="top:205px;">Hello, Little One – Heritage Bowl Candle — $55<br>Hello, Little One – Heritage Large Jar – 400g — $40</p>
      <div class="divider" style="top:245px;"></div>

      <h2 class="range-name" style="top:251px;">LIMITED EDITION RANGE</h2>
      <p class="range-copy" style="top:278px;">Small-batch candles released in limited numbers and<br>available for a short time only.</p>
      <p class="prices" style="top:309px;">Tender Hearts – 200g — $30<br>Forever Yours – Limited Edition – 400g — $40<br>Cubby Cottage – Heritage Bowl Candle — $55</p>
      <div class="divider" style="top:365px;"></div>

      <p class="range-copy" style="top:389px;">Still Ember is an evolving collection. New candle creations are introduced<br>regularly, and this price list may be updated to reflect new offerings and<br>limited releases. Each Still Ember candle is poured slowly and mindfully,<br>with intention at its core — because what we bring into our homes, and into<br>our lives, truly matters.</p>
      <p class="range-copy" style="top:450px;">Our website is currently being built. Online ordering will be available soon. In<br>the meantime, all orders can be placed by contacting us via email at<br><span class="email">hello@stillember.co.</span></p>

      <p class="brand" style="top:541px;">STILL EMBER</p>
    </div>
  </article>

</div>
</body>
</html>
```